Kestin Power Battery advertisment for Facebook ads

Objective:
Design a compelling Facebook advertisement to promote the new Federal Government Home Battery Subsidy, encouraging existing solar customers to act now and install a battery system under the new subsidy program.

Key Message:

25kWh Battery System Installed from $9,800
Act now and secure your affordable energy future today!
Design Requirements:

Bold headline showcasing the 25kWh for $9,800 offer.
Clear reference to the Federal Government Battery Subsidy as the reason for the low pricing.
Include messaging around:
Claim your subsidy before it winds down—like the solar rebate, it reduces each year
The subsidy can only be claimed once per household—go large now to future-proof your energy needs
Add a strong Call to Action like: “Beat the Rush—Secure Your Battery Today!”

Target Market(s)

Home owners who want to add batteries to existing solar systems

Industry/Entity Type

Renewable energy

Colors
0054AA
0677BA
7BADD7
CADEEF
E8F1F8
EB3D1F
EC4F4E
F09395
F8D3D4
FCEDEE

Requirements
Must have
• Visual Style: Modern, clean, and high-trust Use imagery of solar homes, battery units, or families enjoying power security at night Include visual cues of savings, energy independence, or clean energy Mobile-optimized, designed for Facebook feed
Nice to have
• Tone: Confident, future-focused, and urgent—while remaining trustworthy and informative. I would like a picture of battery ideally VOM battery on a home or such
Should not have
• must be professional and be a call to action

```html
<!DOCTYPE html>
<html lang="en">
<head>
<meta charset="UTF-8">
<title>Kestin Power – Home Battery Offer</title>
<link rel="stylesheet" href="https://fonts.googleapis.com/css2?family=Archivo:ital,wdth,wght@0,62..125,100..900;1,62..125,100..900&display=swap">
<style>
  :root{
    --red:#e8130f;
    --deep-red:#8e0c0c;
    --ink:#0b0b0b;
    --paper:#ffffff;
    --mist:#eef3f8;
  }
  *{margin:0;padding:0;box-sizing:border-box}
  html,body{width:1200px;height:1200px;overflow:hidden;background:var(--paper)}
  .ad{
    position:relative;width:1200px;height:1200px;overflow:hidden;
    font-family:"Archivo",Arial,sans-serif;
    background:radial-gradient(circle at 50% 35%,var(--paper) 0%,var(--mist) 45%,var(--paper) 70%);
  }
  .headline{
    position:absolute;left:111px;top:112px;
    font-weight:900;font-size:111px;line-height:102px;letter-spacing:-1px;
    font-stretch:87%;color:var(--ink);
  }
  .headline .accent{color:var(--red)}
  .subsidy{
    position:absolute;left:111px;top:458px;
    font-weight:500;font-size:36px;line-height:44px;font-stretch:110%;color:var(--ink);
  }
  .cta{
    position:absolute;left:111px;top:598px;
    font-weight:600;font-style:italic;font-size:41px;line-height:49px;font-stretch:110%;color:var(--deep-red);
  }
  .home-photo{
    position:absolute;left:0;top:0;width:1200px;height:1200px;
  }
  .brand-name{
    position:absolute;left:78px;top:1060px;
    font-weight:800;font-size:34px;color:var(--paper);letter-spacing:0.5px;
  }
</style>
</head>
<body>
<div class="ad">
  <h1 class="headline">
    <span class="accent">25kWh</span> Home<br>
    Battery Installed<br>
    from <span class="accent">$9,800</span>
  </h1>

  <p class="subsidy">Thanks to the Federal Government<br>Subsidy—Act Now Before It Reduces!</p>

  <p class="cta">Beat the Rush—Secure Your<br>Battery Today!</p>

  <svg class="home-photo" viewBox="0 0 1200 1200">
    <defs>
      <linearGradient id="homeTones" x1="0" y1="0" x2="0" y2="1">
        <stop offset="0" stop-color="#c9d6e2"/>
        <stop offset="0.3" stop-color="#2b3f5a"/>
        <stop offset="0.55" stop-color="#8a8f94"/>
        <stop offset="0.8" stop-color="#b59a7e"/>
        <stop offset="1" stop-color="#5c7a3c"/>
      </linearGradient>
    </defs>
    <path role="img" aria-label="Photo of a brick family home with solar panels on the roof and a battery and inverter mounted on the side wall"
          d="M0 772 C 320 795, 620 705, 1200 708 L1200 1200 L0 1200 Z" fill="url(#homeTones)"/>
    <path d="M0 772 C 320 795, 620 705, 1200 708" fill="none" stroke="var(--red)" stroke-width="7"/>
  </svg>

  <p class="brand-name">Kestin Power</p>
</div>
</body>
</html>
```